Icon-Designs für einzelne Bereiche der Beratung & Erstellung von Webshops
Schnell, zuverlässig, kompetent. Oder wie man's bei Einkäufen in der Bucht sagt: Immer wieder gerne... ;-)
Zielgruppe
Erstellung und Beratung zu Webshops, SEO,SEA usw.
Aufgabenstellung
Einheitliches Design der icons für:
SEO, SEA,Vorlix Firmenplatz, Analytics, Conversion Optimierung, Contentstrategie, Text, Foto/Video, Web-Psychologie, Email-Marketing, Social Media, Klipzo, Webshop-Optimierung, Marketplace Strategie, (= Varendo, Kriva)

```html
<!DOCTYPE html>
<html lang="de">
<head>
<meta charset="utf-8">
<title>Darum kümmern wir uns</title>
<link href="https://fonts.googleapis.com/css2?family=Roboto:wght@300;400;500&display=swap" rel="stylesheet">
<style>
:root{
  --green:#3a9b5c;
  --bg:#edecea;
  --card:#ffffff;
  --ink:#1d1d1d;
  --body:#2a2a2a;
}
*{margin:0;padding:0;box-sizing:border-box}
html,body{width:909px;height:1200px;overflow:hidden;background:#fff;font-family:'Roboto',sans-serif}
.section{background:var(--bg);height:1086px;padding-top:48px}
.intro{text-align:center}
.intro h1{font-weight:500;font-size:24px;letter-spacing:.2px;color:var(--ink);line-height:1.1}
.intro p{font-weight:300;font-size:17px;color:var(--ink);margin-top:1px}
.services{display:grid;grid-template-columns:repeat(4,188px);column-gap:12px;row-gap:13px;width:788px;margin:56px auto 0}
.service{background:var(--card);border:1px solid var(--green);border-radius:5px;height:209px;padding:22px 10px 0;text-align:center}
.service.col2{grid-column:2}
.service-icon{width:60px;height:60px;margin:0 auto;display:block}
.service-icon svg{width:60px;height:60px;stroke:var(--green);fill:none;stroke-width:2;stroke-linecap:round;stroke-linejoin:round}
.service h2{font-weight:400;font-size:12.6px;color:var(--green);margin-top:18px;letter-spacing:.2px}
.service p{font-size:8.6px;line-height:1.27;color:var(--body);margin-top:6px}
.service p + p{margin-top:10px}
.brand-mark{height:60px;display:flex;align-items:center;justify-content:center;gap:8px;color:var(--green);font-weight:500;font-size:17px}
</style>
</head>
<body>
<section class="section">
  <header class="intro">
    <h1>DARUM KÜMMERN WIR UNS</h1>
    <p>für deinen Shop, für deinen Erfolg</p>
  </header>

  <div class="services">
    <article class="service">
      <span class="service-icon"><svg viewBox="0 0 60 60"><rect x="2" y="4" width="56" height="20" rx="3"/><circle cx="33" cy="30" r="11"/><circle cx="33" cy="30" r="6"/><path d="M41 38l9 9"/><path d="M8 12l3 6 3-6 3 6 3-6M24 12l3 6 3-6 3 6 3-6M40 12l3 6 3-6 3 6 3-6"/></svg></span>
      <h2>SEO</h2>
      <p>hre Website hat es verdient, dass sie bei Findora&amp;Co optimal gefunden wird.</p>
      <p>Mit unserer Hilfe katapultieren Sie ihre Website auf die oberen Plätze und erhalten wertvolle Besucher.</p>
    </article>
    <article class="service">
      <span class="service-icon"><svg viewBox="0 0 60 60"><rect x="4" y="6" width="44" height="36" rx="2"/><path d="M4 14h44M8 10h2M13 10h2M22 10h20"/><rect x="10" y="20" width="24" height="13"/><path d="M14 30l3-7 3 7M15 28h4M24 23v7h3a3 3 0 000-7z"/><path d="M36 30l16 8-7 2 6 8-3 2-6-8-4 5z"/></svg></span>
      <h2>SEA</h2>
      <p>Lenken Sie potenzielle Kunden gezielt und ohne Streuverluste auf ihre Website.</p>
      <p>Findora Ads sind ein wunderbares Mittel ganz schnell die gewünschte Zielgruppe zu erreichen.</p>
    </article>
    <article class="service">
      <span class="service-icon"><svg viewBox="0 0 60 60"><path d="M10 6h40l6 20H4z"/><path d="M4 26a7 7 0 0013 0 7 7 0 0013 0 7 7 0 0013 0 7 7 0 0013 0M18 6l-4 20M30 6v20M42 6l4 20"/><path d="M8 33v21h44V33"/></svg></span>
      <h2>VORLIX FIRMENPLATZ</h2>
      <p>Jede dritte Suchanfrage bei Findora hat mittlerweile regionalen oder lokalen Bezug.</p>
      <p>Mit einem optimierten Firmenplatz Eintrag generieren sie im Handumdrehen neue Kunden.</p>
    </article>
    <article class="service">
      <span class="service-icon"><svg viewBox="0 0 60 60"><rect x="3" y="18" width="54" height="30" rx="2"/><path d="M3 42h54M24 48l-2 6h16l-2-6M18 54h24"/><path d="M12 22v10M17 16v16M22 10v22M27 14v18"/><circle cx="46" cy="12" r="8"/><path d="M46 4v8h8"/><path d="M8 36l8-5 8 6 10-7 8 4 10-4"/></svg></span>
      <h2>ANALYTICS</h2>
      <p>Sie wollen sicherlich wissen, wer, wann und wie viele Besucher ihre Website aufsuchen!?</p>
      <p>Egal ob mit Findora Stats oder einem anderen Tool. Wir machen ihre Webbesucher transparent.</p>
    </article>

    <article class="service">
      <span class="service-icon"><svg viewBox="0 0 60 60"><circle cx="30" cy="30" r="10"/><circle cx="30" cy="30" r="6"/><path d="M32 27a3 3 0 100 6M26 29h5M26 31h5"/><path d="M22 24H12l4-4M12 24l4 4M38 36h10l-4-4M48 36l-4 4"/><circle cx="6" cy="34" r="3" fill="currentColor"/><path d="M1 44a5 5 0 0110 0z"/><circle cx="54" cy="20" r="3"/><path d="M49 30a5 5 0 0110 0z"/></svg></span>
      <h2>CONVERSION</h2>
      <p>Viele Besucher auf ihrer Website sind eine schöne Sache. Wichtiger ist es aber, dass diese auch bei ihnen kaufen!</p>
      <p>Ihre wunderbare Produkte oder/und ihren Kunden tollen Dienstleistungen haben es verdient gekauft zu werden.</p>
    </article>
    <article class="service">
      <span class="service-icon"><svg viewBox="0 0 60 60"><path d="M12 2h30v56H12V10z"/><path d="M12 10l8-8v8z"/><circle cx="28" cy="16" r="8"/><path d="M24 14h5l4-3v9l-4-3h-5z"/><path d="M16 34h20M16 40h20M16 46h16"/><path d="M40 56l2-8h6l2 8z" fill="#3a9b5c"/><circle cx="45" cy="42" r="4" fill="#3a9b5c"/></svg></span>
      <h2>CONTENTSTRATEGIE</h2>
      <p>Frage: ist es notwenig, hier noch 2-3 erklärende Zeilen einzufügen</p>
    </article>
    <article class="service">
      <span class="service-icon"><svg viewBox="0 0 60 60"><rect x="8" y="4" width="44" height="52" rx="4"/><path d="M14 18h14M21 18v16M32 20h14M32 27h14M32 34h14M14 42h32M14 48h32"/></svg></span>
      <h2>TEXT</h2>
      <p>Frage: ist es notwenig, hier noch 2-3 erklärende Zeilen einzufügen</p>
    </article>
    <article class="service">
      <span class="service-icon"><svg viewBox="0 0 60 60"><rect x="2" y="8" width="56" height="28"/><rect x="10" y="4" width="40" height="36"/><path d="M10 36l12-14 10 10 6-5 12 9"/><circle cx="36" cy="16" r="3"/><path d="M30 34l2 22 5-6 6 7 3-3-6-6 7-3z"/></svg></span>
      <h2>FOTO / VIDEO</h2>
      <p>Frage: ist es notwenig, hier noch 2-3 erklärende Zeilen einzufügen</p>
    </article>

    <article class="service">
      <span class="service-icon"><svg viewBox="0 0 60 60"><circle cx="30" cy="30" r="24"/><ellipse cx="30" cy="30" rx="11" ry="24"/><path d="M6 20h48M6 40h48M30 6v48"/><path d="M8 26l3 8 3-8 3 8 3-8M24 26l3 8 3-8 3 8 3-8M40 26l3 8 3-8 3 8 3-8"/></svg></span>
      <h2>WEB-PSYCHOLOGIE</h2>
      <p>Frage: ist es notwenig, hier noch 2-3 erklärende Zeilen einzufügen</p>
    </article>
    <article class="service">
      <span class="service-icon"><svg viewBox="0 0 60 60"><path d="M4 26v30h52V26L30 8z"/><path d="M4 56l20-18M56 56L36 38M4 26l18 14M56 26L38 40"/><path d="M18 34V4h16"/><path d="M22 10h6M22 16h6"/><path d="M28 24l12-12 6 12z"/><path d="M46 6l4-4M48 12h6M44 2v-2"/></svg></span>
      <h2>EMAIL-MARKETING</h2>
      <p>Frage: ist es notwenig, hier noch 2-3 erklärende Zeilen einzufügen</p>
    </article>
    <article class="service">
      <span class="service-icon"><svg viewBox="0 0 60 60"><circle cx="44" cy="14" r="7"/><circle cx="16" cy="30" r="7"/><circle cx="44" cy="46" r="7"/><path d="M22 27l16-10M22 33l16 10"/></svg></span>
      <h2>SOCIAL MEDIA</h2>
      <p>Frage: ist es notwenig, hier noch 2-3 erklärende Zeilen einzufügen</p>
    </article>
    <article class="service">
      <div class="brand-mark">Klipzo</div>
      <h2>KLIPZO</h2>
      <p>Frage: ist es notwenig, hier noch 2-3 erklärende Zeilen einzufügen</p>
    </article>

    <article class="service col2">
      <span class="service-icon"><svg viewBox="0 0 60 60"><rect x="3" y="3" width="54" height="54" rx="2"/><path d="M3 10h54M8 7h1M12 7h1M16 7h1"/><rect x="8" y="15" width="11" height="8"/><rect x="24" y="15" width="11" height="8"/><rect x="40" y="15" width="11" height="8"/><path d="M8 28h11M24 28h11M40 28h11M8 32h11M40 32h11"/><path d="M10 52a20 18 0 0140 0z"/><path d="M30 52l6-14"/></svg></span>
      <h2>WEBSHOP-OPTIMIERUNG</h2>
      <p>Frage: ist es notwenig, hier noch 2-3 erklärende Zeilen einzufügen</p>
    </article>
    <article class="service">
      <div class="brand-mark"><span>Varendo</span><span>Kriva</span></div>
      <h2>MARKETPLACE STRATEGIE</h2>
      <p>Frage: ist es notwenig, hier noch 2-3 erklärende Zeilen einzufügen</p>
    </article>
  </div>
</section>
</body>
</html>
```